Website Redesign - Money is Guaranteed!

I would like a site similar to this: http://www.givewheelsforheroes.example

old site: http://www.autosforpatriots.example

Create a professional website; a car donation site seeking leads to return calls.

Please see http://www.givewheelsforheroes.example for the concept I am after.

The webpage should have a professional feel. The pages to include are 'Home', 'About us' and 'Get Started'

Industry/Entity Type

It Professional

Coding

Coded - Design and coding required

Number of Pages Required

1 page

```html
<!DOCTYPE html>
<html lang="en">
<head>
<meta charset="utf-8">
<title>Autos for Patriots – Donate Your Car</title>
<link href="https://fonts.googleapis.com/css2?family=Open+Sans:wght@400;600;700&family=Roboto+Slab:wght@400;500&display=swap" rel="stylesheet">
<style>
:root{
  --blue-dark:#0b3f7f;
  --blue:#1f5ea8;
  --blue-title:#1a5ea8;
  --blue-why-a:#0a3a86;
  --blue-why-b:#1a5cc0;
  --footer:#0a4a9a;
  --red:#8c0f13;
  --red-title:#8b0f12;
  --red-bright:#c4161c;
  --ink:#333;
  --muted:#555;
  --white:#fff;
}
*{box-sizing:border-box;margin:0;padding:0}
html,body{width:1200px;height:2276px;overflow:hidden}
body{font-family:"Open Sans",Arial,sans-serif;color:var(--ink);background:#fff;position:relative}
.heading{font-family:"Roboto Slab",Georgia,serif;font-weight:500}
section,header,footer{position:absolute;left:0;width:1200px}

/* header */
.site-header{top:0;height:112px;background:linear-gradient(#2366b3,var(--blue-dark))}
.brand{position:absolute;left:132px;top:36px;display:flex;align-items:center;gap:10px;color:var(--white);font-weight:600;font-size:20px;letter-spacing:.5px}
.brand-mark{width:26px;height:26px;background:var(--red-bright)}
.toll{position:absolute;left:778px;top:20px;display:flex;align-items:center;gap:14px;color:var(--white);font-weight:700;font-size:14px}
.toll .phone-dot{width:30px;height:30px;border-radius:50%;background:var(--red-bright);display:flex;align-items:center;justify-content:center}
.toll .num{font-size:15px}
.main-nav a{position:absolute;top:72px;color:var(--white);font-size:13px;font-weight:600;text-decoration:none;white-space:nowrap}
.main-nav a.active::after{content:"";position:absolute;left:-6px;right:-6px;top:32px;height:3px;background:var(--red-bright)}

/* hero */
.hero{top:112px;height:425px;background:linear-gradient(#f2f2f2,#d4d4d4)}
.hero-title{position:absolute;left:132px;top:24px;font-size:28px;line-height:35px;color:var(--red-title)}
.hero-photo{position:absolute;left:53px;top:108px;width:628px;height:317px;background:linear-gradient(90deg,#6b6a4c 0%,#8a7f6e 35%,#c9c9c9 55%,#9c1b22 75%,#c7c7c7 100%)}
.donate-form{position:absolute;left:681px;top:0;width:385px;height:425px;background:var(--red);color:var(--white);text-align:center}
.donate-form h2{margin-top:28px;font-size:29px;letter-spacing:1.5px;font-weight:500}
.donate-form h3{font-size:20px;letter-spacing:1px;font-weight:500;margin-top:2px}
.field{position:absolute;background:#fff;border-radius:3px;height:41px;font-size:11px;color:#777;text-align:left;padding:13px 11px}
.field.select::after{content:"";position:absolute;right:14px;top:15px;width:7px;height:7px;border-right:2px solid #444;border-bottom:2px solid #444;transform:rotate(45deg)}
.btn-donate{position:absolute;left:30px;top:326px;width:328px;height:46px;background:linear-gradient(#3a3a3a,#1e1e1e);border-radius:3px;color:#fff;font-weight:700;font-size:19px;line-height:46px;letter-spacing:.5px}

/* how it works */
.how{top:537px;height:367px}
.section-title{position:absolute;left:0;width:1200px;text-align:center;font-size:29px}
.how .section-title{top:40px;color:var(--blue-title)}
.how-intro{position:absolute;left:215px;width:770px;top:98px;text-align:center;font-size:12px;line-height:24px;color:var(--muted)}
.step{position:absolute;top:198px;width:320px}
.step svg{position:absolute;left:0;top:0}
.step h4{position:absolute;left:67px;top:0;font-size:19px;color:var(--red-title);white-space:nowrap}
.step p{position:absolute;left:70px;top:39px;width:215px;font-size:12px;line-height:24px;color:var(--muted);text-align:justify}

/* why */
.why{top:904px;height:701px;background:radial-gradient(ellipse at 50% 40%,var(--blue-why-b),var(--blue-why-a) 70%)}
.why .section-title{top:68px;color:var(--white)}
.reason{position:absolute;width:280px;text-align:center;color:var(--white)}
.reason .icon{height:44px;display:flex;align-items:flex-end;justify-content:center}
.reason h4{margin-top:24px;font-size:19px;font-weight:500;white-space:nowrap}
.reason p{margin-top:12px;font-size:12px;line-height:24px;padding:0 8px}

/* program */
.program{top:1605px;height:431px;background:#fff}
.program .title{position:absolute;left:130px;top:78px;font-size:29px;color:var(--blue-title)}
.program ul{position:absolute;left:132px;top:143px;list-style:none}
.program li{font-family:"Roboto Slab",Georgia,serif;font-size:14px;height:29px;display:flex;align-items:center;gap:20px;color:#333;letter-spacing:.3px}
.program li .bullet{width:14px;height:14px;border-radius:50%;background:var(--red);position:relative}
.program li .bullet::after{content:"";position:absolute;left:3px;top:4.5px;width:4px;height:4px;border-right:1.5px solid #fff;border-top:1.5px solid #fff;transform:rotate(45deg)}
.badge-secure{position:absolute;left:137px;top:294px;width:139px;height:53px;background:#eee;border-radius:4px}
.badge-charity{position:absolute;left:318px;top:291px;width:61px;height:61px;border-radius:50%;background:#cfe0ee;border:3px solid #3a84bf}
.program-photo{position:absolute;left:604px;top:0;width:493px;height:431px;background:linear-gradient(#8a8b78,#6f705e 50%,#9a9a88)}
.laptop-screen{position:absolute;left:692px;top:108px;width:316px;height:178px;background:linear-gradient(#a3151a,#d0262c);border:7px solid #2b2b2b;color:#fff;text-align:center}
.laptop-screen h5{font-weight:600;font-size:18px;margin-top:20px}
.laptop-screen p{font-size:11.5px;line-height:19px}
.laptop-screen .lines{margin-top:10px}

/* footer */
.site-footer{top:2036px;height:240px;background:var(--footer);color:#fff}
.site-footer .brand{top:38px}
.copyright{position:absolute;left:132px;top:112px;font-size:11px}
.footer-col h6{position:absolute;top:40px;font-size:19px;font-weight:500;font-family:"Roboto Slab",Georgia,serif}
.quick a{position:absolute;left:486px;color:#fff;text-decoration:none;font-size:12px}
.contact-item{position:absolute;left:692px;display:flex;gap:10px;font-size:11.5px;line-height:16px;width:210px}
.contact-item svg{flex:none;margin-top:2px}
.social{position:absolute;left:925px;top:39px;display:flex;gap:5px}
.social span{width:33px;height:33px;border-radius:50%;border:2px solid #fff}
</style>
</head>
<body>

<header class="site-header">
  <div class="brand"><span class="brand-mark"></span>AUTOS for PATRIOTS</div>
  <div class="toll">CALL TOLL-FREE
    <span class="phone-dot"><svg width="14" height="14" viewBox="0 0 24 24"><path fill="#fff" d="M6.6 10.8a15.1 15.1 0 0 0 6.6 6.6l2.2-2.2c.3-.3.7-.4 1-.2 1.1.4 2.3.6 3.6.6.6 0 1 .4 1 1V20c0 .6-.4 1-1 1A17 17 0 0 1 3 4c0-.6.4-1 1-1h3.5c.6 0 1 .4 1 1 0 1.3.2 2.5.6 3.6.1.3 0 .7-.2 1z"/></svg></span>
    <span class="num">1-800-555-0142</span>
  </div>
  <nav class="main-nav">
    <a class="active" href="#" style="left:539px">Home</a>
    <a href="#" style="left:623px">About us</a>
    <a href="#" style="left:726px">Why autosforpatriots</a>
    <a href="#" style="left:900px">Program</a>
    <a href="#" style="left:1001px">Contact us</a>
  </nav>
</header>

<section class="hero">
  <h1 class="hero-title heading">Donate Your Car to Veterans<br>and Get a Tax Deduction</h1>
  <div class="hero-photo" role="img" aria-label="Photo of a soldier holding a US flag with a child, beside a red car"></div>
  <form class="donate-form">
    <h2 class="heading">Donate Your Car</h2>
    <h3 class="heading">Running or Not</h3>
    <div class="field" style="left:30px;top:108px;width:157px">First Name</div>
    <div class="field" style="left:200px;top:108px;width:158px">Last Name</div>
    <div class="field" style="left:30px;top:158px;width:328px">Phone Number</div>
    <div class="field" style="left:30px;top:211px;width:328px">Email Address</div>
    <div class="field select" style="left:30px;top:263px;width:157px">Make of Car</div>
    <div class="field select" style="left:200px;top:263px;width:158px">Model of Car</div>
    <div class="btn-donate">DONATE NOW</div>
  </form>
</section>

<section class="how">
  <h2 class="section-title heading">How it Work</h2>
  <p class="how-intro">Should you have other questions or concerns about these privacy policies or would like to opt out of future emails, phone calls, or other<br>direct communications, please call us at 1-800-555-0187.</p>

  <div class="step" style="left:133px">
    <svg width="48" height="44" viewBox="0 0 48 44"><rect x="3" y="8" width="32" height="32" rx="5" fill="none" stroke="#1a5ea8" stroke-width="4"/><path d="M16 28l3-9L38 0l7 7-19 19z" fill="#1a5ea8" stroke="#fff" stroke-width="2"/></svg>
    <h4 class="heading">Fill out the simple form</h4>
    <p>Free 24/7 Pickup with No DMV Hassles. Complete the form and a representative will call you</p>
  </div>
  <div class="step" style="left:455px">
    <svg width="56" height="44" viewBox="0 0 56 44"><path d="M8 20l6-14h28l6 14h2a4 4 0 0 1 4 4v10H2V24a4 4 0 0 1 4-4z" fill="#1a5ea8"/><path d="M14 20l4-9h20l4 9z" fill="#fff"/><rect x="6" y="34" width="10" height="8" rx="2" fill="#1a5ea8"/><rect x="40" y="34" width="10" height="8" rx="2" fill="#1a5ea8"/><circle cx="12" cy="27" r="3" fill="#fff"/><circle cx="44" cy="27" r="3" fill="#fff"/></svg>
    <h4 class="heading">Schedule your pick-up</h4>
    <p>We will pick up your car donation, running or not, when it's most convenient, at home or work.</p>
  </div>
  <div class="step" style="left:786px">
    <svg width="48" height="50" viewBox="0 0 48 50"><path d="M2 2h20v8H10v30H2z" fill="#1a5ea8"/><path d="M14 12h20l10 10v26H14z" fill="none" stroke="#1a5ea8" stroke-width="4"/><path d="M32 12v12h12" fill="#1a5ea8"/></svg>
    <h4 class="heading">Receive tax deduction</h4>
    <p>We issue you an IRS tax receipt &amp; offer the largest resale network to get you the highest tax write-off possible.</p>
  </div>
</section>

<section class="why" role="region" aria-label="Why donate, over a background of waving flags">
  <h2 class="section-title heading">Why Donate Your Car to Us?</h2>

  <div class="reason" style="left:130px;top:160px">
    <div class="icon"><svg width="50" height="40" viewBox="0 0 50 40"><rect x="17" y="1" width="16" height="8" rx="2" fill="none" stroke="#fff" stroke-width="3"/><rect x="1" y="8" width="48" height="31" rx="4" fill="#fff"/><rect x="1" y="20" width="48" height="3" fill="#1a4fa8"/><rect x="21" y="17" width="8" height="8" fill="#fff"/></svg></div>
    <h4 class="heading">Income Tax Deduction</h4>
    <p>We issue you an IRS tax receipt &amp; offer the largest resale network to get you the highest tax write-off possible.</p>
  </div>
  <div class="reason" style="left:461px;top:160px">
    <div class="icon"><svg width="42" height="42" viewBox="0 0 42 42"><path d="M1 1h40v26L27 41H1z" fill="#fff"/><path d="M27 41V27h14" fill="#1a4fa8"/></svg></div>
    <h4 class="heading">No Paperwork Hassles</h4>
    <p>We issue you an IRS tax receipt &amp; offer the largest resale network to get you the highest tax write-off possible.</p>
  </div>
  <div class="reason" style="left:811px;top:160px">
    <div class="icon"><svg width="42" height="44" viewBox="0 0 42 44"><ellipse cx="21" cy="7" rx="20" ry="6" fill="#fff"/><path d="M1 12c0 4 9 7 20 7s20-3 20-7v8c0 4-9 7-20 7S1 24 1 20z" fill="#fff"/><path d="M1 25c0 4 9 7 20 7s20-3 20-7v11c0 4-9 7-20 7S1 40 1 36z" fill="#fff"/></svg></div>
    <h4 class="heading">Help fund programs</h4>
    <p>We issue you an IRS tax receipt &amp; offer the largest resale network to get you the highest tax write-off possible.</p>
  </div>

  <div class="reason" style="left:130px;top:402px">
    <div class="icon"><svg width="30" height="42" viewBox="0 0 30 42"><path d="M15 1a14 14 0 0 1 14 14c0 10-14 26-14 26S1 25 1 15A14 14 0 0 1 15 1z" fill="#fff"/><circle cx="15" cy="15" r="5" fill="#1a4fa8"/></svg></div>
    <h4 class="heading">Free Local Towing</h4>
    <p>We issue you an IRS tax receipt &amp; offer the largest resale network to get you the highest tax write-off possible.</p>
  </div>
  <div class="reason" style="left:461px;top:402px">
    <div class="icon"><svg width="44" height="40" viewBox="0 0 44 40"><path d="M3 21l7-7 8 8L34 4l7 7-23 24z" fill="#fff"/></svg></div>
    <h4 class="heading">All Cars Accepted</h4>
    <p>We issue you an IRS tax receipt &amp; offer the largest resale network to get you the highest tax write-off possible.</p>
  </div>
  <div class="reason" style="left:811px;top:402px">
    <div class="icon"><svg width="42" height="42" viewBox="0 0 42 42"><circle cx="21" cy="21" r="18" fill="none" stroke="#fff" stroke-width="5"/><path d="M21 10v12h9" fill="none" stroke="#fff" stroke-width="4"/></svg></div>
    <h4 class="heading">Schedule a Free Pickup</h4>
    <p>We issue you an IRS tax receipt &amp; offer the largest resale network to get you the highest tax write-off possible.</p>
  </div>
</section>

<section class="program">
  <h2 class="title heading">Car Donation Program</h2>
  <ul>
    <li><span class="bullet"></span>DONATION ACCEPTED NATIONALWIDE</li>
    <li><span class="bullet"></span>ALL VECHICLE TYPES</li>
    <li><span class="bullet"></span>TAX DEDUCTION</li>
    <li><span class="bullet"></span>TOWING IS FREE</li>
  </ul>
  <div class="badge-secure" role="img" aria-label="Security certification badge"></div>
  <div class="badge-charity" role="img" aria-label="Approved charity badge"></div>
  <div class="program-photo" role="img" aria-label="Photo of a soldier in camouflage uniform holding an open laptop"></div>
  <div class="laptop-screen">
    <h5>DONATE YOUR CAR TODAY!</h5>
    <div class="lines">
      <p>You have no costs.</p>
      <p>Free towing, running or not.</p>
      <p>We issue you an IRS tax receipt.</p>
      <p>We take care of all paperwork.</p>
      <p>And we take care of DMV &amp; Smog issues.</p>
    </div>
  </div>
</section>

<footer class="site-footer">
  <div class="brand"><span class="brand-mark"></span>AUTOS for PATRIOTS</div>
  <p class="copyright">Copyright © 2017, autosforpatriots.example</p>

  <div class="footer-col quick">
    <h6 style="left:484px">QUICK LINKS</h6>
    <a href="#" style="top:88px">Home</a>
    <a href="#" style="top:111px">About us</a>
    <a href="#" style="top:135px">Why autosforpatriots</a>
    <a href="#" style="top:159px">Program</a>
    <a href="#" style="top:183px">Contact us</a>
  </div>

  <div class="footer-col">
    <h6 style="left:692px">CONTACT US</h6>
    <div class="contact-item" style="top:88px"><svg width="12" height="12" viewBox="0 0 12 12"><rect x="1" y="4" width="10" height="7" fill="#fff"/><path d="M0 4c2-3 10-3 12 0" stroke="#fff" stroke-width="2" fill="none"/></svg>(555) 013-4410</div>
    <div class="contact-item" style="top:114px"><svg width="12" height="12" viewBox="0 0 12 12"><rect x="3" y="0" width="6" height="4" fill="#fff"/><rect x="0" y="4" width="12" height="5" fill="#fff"/><rect x="3" y="8" width="6" height="4" fill="#fff"/></svg>(555) 013-4411</div>
    <div class="contact-item" style="top:142px"><svg width="12" height="10" viewBox="0 0 12 10"><rect x="0" y="0" width="12" height="10" fill="#fff"/><path d="M0 0l6 5 6-5" stroke="#0a4a9a" fill="none"/></svg><span style="text-decoration:underline">info@autosforpatriots.example</span></div>
    <div class="contact-item" style="top:170px"><svg width="10" height="14" viewBox="0 0 10 14"><path d="M5 0a5 5 0 0 1 5 5c0 4-5 9-5 9S0 9 0 5a5 5 0 0 1 5-5z" fill="#fff"/></svg><span>#2868 Lorem ipsum dolor sit<br>amet, consectetur</span></div>
  </div>

  <div class="social" aria-label="Social links"><span></span><span></span><span></span><span></span></div>
</footer>

</body>
</html>
```